Morvela Aesthetic Doctor

I require an elegant, luxurious looking business card for my aesthetic business. I am a doctor and that will set me aside from competitors. I am planning to provide home and spa based treatments to clients with high expectations. I have attached my logo.

```html
<!DOCTYPE html>
<html lang="en">
<head>
<meta charset="utf-8">
<title>Morvela Aesthetic Doctor – Business Card</title>
<link href="https://fonts.googleapis.com/css2?family=Arimo:wght@400;700&family=Cinzel:wght@400&display=swap" rel="stylesheet">
<style>
  :root {
    --sky: #7dc9eb;
    --sky-deep: #3ea6de;
    --stone: #a7a9ac;
    --stone-dark: #8e9093;
    --paper: #ffffff;
    --backdrop: #2a2a2a;
  }
  * { box-sizing: border-box; margin: 0; padding: 0; }
  html, body { width: 1200px; height: 1015px; overflow: hidden; }
  body { background: var(--backdrop); position: relative; font-family: "Arimo", Arial, sans-serif; }

  .card { position: absolute; width: 760px; height: 434px; overflow: hidden; background: var(--paper);
          box-shadow: 0 10px 30px rgba(0,0,0,.55); }
  .card--front { left: 70px; top: 55px; }
  .card--back { left: 370px; top: 525px; }
  .card__shape { position: absolute; inset: 0; width: 100%; height: 100%; }

  .brand { position: absolute; left: 70px; top: 170px; display: flex; align-items: center; gap: 18px; }
  .brand__mark { width: 74px; height: 74px; border-radius: 50%; border: 3px solid var(--stone); flex: none; }
  .brand__name { font-family: "Cinzel", Georgia, serif; font-weight: 400; color: var(--stone-dark); line-height: 1; }
  .brand__title { display: block; font-size: 52px; letter-spacing: 2px; }
  .brand__tagline { display: block; font-size: 18px; letter-spacing: 2px; margin-top: 6px; }

  .services { position: absolute; right: 36px; top: 48px; list-style: none; text-align: right;
              color: var(--paper); font-size: 17px; line-height: 25px; letter-spacing: .3px; }
  .services li::after { content: ""; display: inline-block; width: 9px; height: 9px; border-radius: 50%;
                        background: var(--paper); margin-left: 8px; vertical-align: 2px; }
  .services li.services__cont::after { visibility: hidden; }

  .doctor { position: absolute; right: 40px; top: 42px; text-align: right; color: var(--paper); }
  .doctor__name { font-size: 26px; font-weight: 700; }
  .doctor__post { font-size: 15px; font-weight: 400; margin-left: 4px; }
  .doctor__cred { font-size: 17px; line-height: 21px; margin-top: 6px; }

  .social { position: absolute; right: 52px; top: 180px; display: flex; gap: 8px; }
  .social__dot { width: 30px; height: 30px; border-radius: 50%; border: 2px solid var(--paper); }

  .contact { position: absolute; right: 38px; top: 290px; list-style: none; text-align: right;
             color: var(--paper); font-size: 18px; line-height: 26px; }
  .contact li { display: flex; justify-content: flex-end; align-items: center; gap: 8px; }
  .contact svg { width: 17px; height: 17px; flex: none; }
</style>
</head>
<body>

<section class="card card--front" aria-label="Business card front">
  <svg class="card__shape" viewBox="0 0 760 434" aria-hidden="true">
    <rect width="760" height="434" fill="var(--sky)"/>
    <circle cx="215" cy="250" r="300" fill="var(--paper)"/>
    <path d="M 330 -20 A 312 312 0 0 1 420 470" fill="none" stroke="var(--stone)" stroke-width="5"/>
  </svg>
  <div class="brand">
    <span class="brand__mark"></span>
    <span class="brand__name">
      <span class="brand__title">MORVELA</span>
      <span class="brand__tagline">AESTHETIC DOCTOR</span>
    </span>
  </div>
  <ul class="services">
    <li>DERMAL INJECTABLES</li>
    <li>PLASMA FACIALS</li>
    <li>MICRONEEDLING</li>
    <li>SKIN BOOSTERS</li>
    <li>EXCESSIVE SWEATING</li>
    <li>HOME AND SPA</li>
    <li class="services__cont">BASED TREATMENTS</li>
  </ul>
</section>

<section class="card card--back" aria-label="Business card back">
  <svg class="card__shape" viewBox="0 0 760 434" aria-hidden="true">
    <rect width="760" height="434" fill="var(--stone)"/>
    <circle cx="215" cy="290" r="300" fill="var(--paper)"/>
    <path d="M 300 -5 A 312 312 0 0 1 430 480" fill="none" stroke="var(--sky)" stroke-width="5"/>
  </svg>
  <div class="brand" style="top: 190px;">
    <span class="brand__mark"></span>
    <span class="brand__name">
      <span class="brand__title">MORVELA</span>
      <span class="brand__tagline">AESTHETIC DOCTOR</span>
    </span>
  </div>
  <div class="doctor">
    <p class="doctor__name">Dr Elin Varga<span class="doctor__post">MRCPCH MD</span></p>
    <p class="doctor__cred">Australasian Diploma of<br>Aesthetic Medicine</p>
  </div>
  <div class="social" aria-label="Social profiles">
    <span class="social__dot"></span>
    <span class="social__dot"></span>
  </div>
  <ul class="contact">
    <li>0800 555 014
      <svg viewBox="0 0 24 24" aria-hidden="true"><path d="M6 2l4 4-2.5 2.5a13 13 0 0 0 8 8L18 14l4 4-3 3C10 21 3 14 3 5z" fill="var(--paper)"/></svg>
    </li>
    <li>elin@morvela.co.nz
      <svg viewBox="0 0 24 24" aria-hidden="true"><rect x="2" y="5" width="20" height="14" fill="var(--paper)"/><path d="M2 5l10 8 10-8" fill="none" stroke="var(--stone)" stroke-width="1.8"/></svg>
    </li>
    <li>www.morvela.co.nz
      <svg viewBox="0 0 24 24" aria-hidden="true"><g fill="none" stroke="var(--paper)" stroke-width="2"><circle cx="12" cy="12" r="10"/><ellipse cx="12" cy="12" rx="4.5" ry="10"/><path d="M2 12h20"/></g></svg>
    </li>
  </ul>
</section>

</body>
</html>
```